Wound Care Flyer

Looking for a Trifold brochure that is modern and has a high aesthetic. (Specialty services) Would like the colors to center around Black and Gold. Possibly updating the logo. Attached is the old brochure and a document about our services.

```html
<!DOCTYPE html>
<html lang="en">
<head>
<meta charset="utf-8">
<title>Fernhill Wounds – Trifold Brochure</title>
<link rel="stylesheet" href="https://fonts.googleapis.com/css2?family=Arimo:wght@400;500;600&family=Roboto+Condensed:wght@400&family=Roboto:wght@100;300;400&display=swap">
<style>
:root{
  --backdrop:#e2e2e4;
  --paper:#ffffff;
  --ink:#070707;
  --gold:#c6a05c;
  --gold-bright:#e2b548;
  --text:#1c1c1c;
  --body:#3c3c3c;
  --rule:#d9c7a4;
  --rule-dark:#3a3a3a;
  --white:#ffffff;
}
*{margin:0;padding:0;box-sizing:border-box}
html,body{width:912px;height:1200px;overflow:hidden}
body{background:radial-gradient(ellipse at 50% 40%,#ececee 0%,var(--backdrop) 70%);font-family:"Arimo",Arial,sans-serif;color:var(--text);position:relative}
.sheet{position:absolute;left:107px;width:686px;height:529px;background:var(--paper);overflow:hidden;box-shadow:0 2px 10px rgba(0,0,0,.18)}
.sheet--outside{top:68px}
.sheet--inside{top:619px}
.abs{position:absolute}
.art{position:absolute;left:0;top:0;width:686px;height:529px}
.fold{position:absolute;top:0;height:529px;width:229px;pointer-events:none}
.fold--left{left:0;background:linear-gradient(90deg,rgba(0,0,0,0) 80%,rgba(0,0,0,.05))}
.fold--mid{left:226px;background:linear-gradient(90deg,rgba(0,0,0,.06),rgba(0,0,0,0) 15%,rgba(0,0,0,0) 85%,rgba(0,0,0,.05))}
.pill{position:absolute;height:18px;border-radius:9px;background:var(--ink);color:var(--white);font-size:12px;line-height:18px;text-align:center;white-space:nowrap}
.pill--outline{border:1px solid var(--rule);line-height:16px}
.rule{position:absolute;height:1px;background:var(--gold)}

/* brand name */
.brand-name{position:absolute;text-align:center;color:var(--white);font-family:"Arimo",Arial,sans-serif;font-weight:400;white-space:nowrap}
.brand-name--cover{left:455px;width:231px;top:160px;font-size:24px;line-height:28px}
.brand-name--panel{left:0;width:222px;top:82px;font-size:21px;line-height:26px}
.brand-name--small{color:var(--text);font-size:13px;line-height:16px}

/* outside panel 1 */
.feature{position:absolute;left:62px;font-size:17px;line-height:20px;color:var(--white)}
.feature-icon{position:absolute;left:23px;width:22px;height:22px}
.feature-rule{position:absolute;left:23px;width:168px;height:1px;background:#5d5140}
.about-heading{left:18px;top:238px;font-size:12px;line-height:14.5px;color:var(--text)}
.about-body{left:19px;top:279px;font-size:10.3px;line-height:12.5px;color:var(--body)}
.offer-note{left:21px;top:460px;font-family:"Roboto Condensed",sans-serif;font-size:10.2px;line-height:12.5px;color:var(--gold-bright)}

/* outside panel 2 */
.portrait{position:absolute;left:226px;top:0;width:229px;height:240px;background:linear-gradient(180deg,#d4d6d8 0%,#e6e6e6 45%,#f4f4f4 75%,#ffffff 100%)}
.provider-name{left:226px;width:229px;top:303px;text-align:center;font-size:16px;line-height:20px;color:var(--text)}
.contact-intro{left:226px;width:229px;top:385px;text-align:center;font-size:10.3px;line-height:12.7px;font-weight:500;color:var(--text)}
.contact-lines{left:226px;width:229px;top:457px;text-align:center;font-size:10.3px;line-height:15.6px;color:var(--text)}
.contact-lines svg{width:9px;height:9px;vertical-align:-1px;margin-right:3px}

/* outside panel 3 */
.cover{position:absolute;left:455px;top:0;width:231px;height:529px;background:linear-gradient(180deg,#1a1a1a 0%,#0b0b0b 45%,#050505 100%)}
.cover-title{font-family:"Roboto",sans-serif;font-weight:300;color:var(--white);position:absolute;white-space:nowrap}
.cover-title--advanced{left:488px;top:330px;font-size:38px;line-height:38px;letter-spacing:-1.2px}
.cover-title--wound{right:37px;top:361px;font-size:31px;line-height:32px;color:var(--gold);font-weight:400;letter-spacing:-.5px}
.cover-title--care{left:487px;top:365px;font-size:80px;line-height:80px;font-weight:100;letter-spacing:-2px}
.cover-email{left:492px;width:157px;top:481px;height:19px;line-height:17px;border-radius:10px;border:1px solid var(--rule);background:transparent;font-size:10.3px}

/* inside panel 1 */
.mobile-body{left:6px;width:224px;top:223px;text-align:center;font-size:9.8px;line-height:11.25px;color:var(--text)}

/* inside panel 2 */
.leaders-title{left:226px;width:240px;top:13px;text-align:center;font-size:12px;line-height:14px;color:var(--text)}
.services-intro{left:226px;width:240px;top:51px;text-align:center;font-size:9.8px;line-height:11.2px;color:var(--text)}
.treatment-photo{position:absolute;left:285px;top:136px;width:122px;height:122px;border-radius:50%;background:radial-gradient(circle at 55% 45%,#f1e0d4 0%,#d9c2b5 35%,#aeb9c6 70%,#8e9aa8 100%)}
.service-list{position:absolute;left:255px;top:262px;width:190px;list-style:none}
.service-list li{position:relative;padding:4.5px 0 4.5px 7px;border-bottom:1px solid var(--rule-dark);font-size:9.8px;line-height:12px;font-weight:500;color:var(--white)}
.service-list li::before{content:"";position:absolute;left:0;top:9px;width:3px;height:3px;border-radius:50%;background:var(--gold)}

/* inside panel 3 */
.plan-text{left:466px;width:210px;text-align:center;font-size:9.6px;line-height:10.4px;color:var(--white)}
.benefit-title{position:absolute;left:498px;font-size:11.4px;line-height:14px;color:var(--gold)}
.benefit-icon{position:absolute;left:470px;width:20px;height:20px}
.benefit-body{position:absolute;left:471px;width:214px;font-size:9.5px;line-height:10.3px;color:var(--text);white-space:nowrap}
.benefit-rule{position:absolute;left:466px;width:220px;height:1px;background:#dcdcdc}
</style>
</head>
<body>

<!-- OUTSIDE -->
<section class="sheet sheet--outside">
  <div class="portrait" role="img" aria-label="Photo of the nurse practitioner in a white coat standing in a bright clinic"></div>

  <svg class="art" viewBox="0 0 686 529" aria-hidden="true">
    <defs>
      <linearGradient id="goldRing" x1="0" y1="0" x2="1" y2="1">
        <stop offset="0" stop-color="#8a6a35"/>
        <stop offset=".5" stop-color="#e6c98a"/>
        <stop offset="1" stop-color="#b48a45"/>
      </linearGradient>
    </defs>
    <circle cx="104" cy="19" r="179" fill="url(#goldRing)"/>
    <circle cx="101" cy="16" r="176" fill="var(--ink)"/>
    <path d="M0 437 Q205 437 248 529 L0 529 Z" fill="var(--ink)"/>
    <line x1="262" y1="325" x2="420" y2="325" stroke="#b5b5b5" stroke-width="1"/>
    <line x1="286" y1="440" x2="396" y2="440" stroke="var(--gold)" stroke-width="1"/>
  </svg>

  <svg class="feature-icon" style="top:29px" viewBox="0 0 22 22" fill="none" stroke="var(--gold)" stroke-width="1.3" aria-hidden="true"><path d="M3 11 L11 4 L19 11 M5 9.5 V19 H17 V9.5 M9 19 V13 H13 V19"/></svg>
  <div class="feature" style="top:30px">Convenient</div>
  <div class="feature-rule" style="top:60px"></div>
  <svg class="feature-icon" style="top:70px" viewBox="0 0 22 22" fill="none" stroke="var(--gold)" stroke-width="1.3" aria-hidden="true"><path d="M11 18 C4 13 2 10 2 7 C2 4.5 4 3 6.2 3 C8.4 3 10 4.6 11 6.2 C12 4.6 13.6 3 15.8 3 C18 3 20 4.5 20 7 C20 10 18 13 11 18 Z"/></svg>
  <div class="feature" style="top:71px">Compassionate</div>
  <div class="feature-rule" style="top:101px"></div>
  <svg class="feature-icon" style="top:111px" viewBox="0 0 22 22" fill="none" stroke="var(--gold)" stroke-width="1.3" aria-hidden="true"><rect x="2.5" y="2.5" width="17" height="17" rx="3"/><path d="M11 6.5 V15.5 M6.5 11 H15.5"/></svg>
  <div class="feature" style="top:112px">Professional Care</div>
  <div class="feature-rule" style="top:142px"></div>

  <div class="pill" style="left:18px;top:215px;width:70px">About Us</div>
  <p class="abs about-heading">Providing Excellence in<br>Mobile Advanced Wound Care</p>
  <div class="rule" style="left:18px;top:270px;width:185px"></div>
  <p class="abs about-body">Fernhill Wounds brings high-quality,<br>in-home wound care to the greater<br>North Houston area. By integrating<br>advanced technologies, including<br>biologic skin substitutes and negative<br>pressure wound therapy, we ensure the<br>most effective healing methods for<br>patients. We prioritize collaboration<br>with the patient’s healthcare team,<br>including home health services and<br>PCPs, ensuring personalized care<br>without duplicating efforts.</p>
  <p class="abs offer-note">We offer a range of advanced<br>wound care treatments and emphasize<br>patient education, promoting better<br>self-care and faster recovery.</p>

  <p class="brand-name brand-name--small" style="left:226px;width:229px;top:265px">Fernhill Wounds</p>
  <p class="abs provider-name">Dana Whitfield, FNP-C</p>
  <div class="pill" style="left:297px;top:352px;width:87px;height:19px;line-height:19px">Contact Us</div>
  <p class="abs contact-intro">For more information or<br>to schedule an appointment,<br>contact us today:</p>
  <p class="abs contact-lines">
    <svg viewBox="0 0 10 10" fill="none" stroke="#8a8a8a" stroke-width="1"><path d="M2 1 L4 1 L4.8 3 L3.6 4 C4.2 5.2 4.8 5.8 6 6.4 L7 5.2 L9 6 L9 8 C9 8.6 8.6 9 8 9 C4.2 8.8 1.2 5.8 1 2 C1 1.4 1.4 1 2 1 Z"/></svg>Phone: (555) 014-2290<br>
    <svg viewBox="0 0 10 10" fill="none" stroke="#8a8a8a" stroke-width="1"><rect x="2.5" y="1" width="5" height="3"/><rect x="1" y="4" width="8" height="3.5"/><rect x="2.5" y="6.5" width="5" height="2.5"/></svg>(555) 014-7718<br>
    <svg viewBox="0 0 10 10" fill="none" stroke="#8a8a8a" stroke-width="1"><rect x="1" y="2" width="8" height="6"/><path d="M1 2 L5 5.5 L9 2"/></svg>fernhillwounds@example.com
  </p>

  <div class="cover"></div>
  <svg class="art" viewBox="0 0 686 529" aria-hidden="true">
    <path d="M455 318 Q571 212 686 318 L686 529 L455 529 Z" fill="#020202"/>
    <path d="M455 318 Q571 212 686 318" fill="none" stroke="url(#goldRing)" stroke-width="3"/>
  </svg>
  <p class="brand-name brand-name--cover">Fernhill Wounds</p>
  <p class="cover-title cover-title--advanced">Advanced</p>
  <p class="cover-title cover-title--wound">Wound</p>
  <p class="cover-title cover-title--care">Care</p>
  <div class="pill cover-email">fernhillwounds@example.com</div>

  <div class="fold fold--left"></div>
  <div class="fold fold--mid"></div>
</section>

<!-- INSIDE -->
<section class="sheet sheet--inside">
  <svg class="art" viewBox="0 0 686 529" aria-hidden="true">
    <defs>
      <linearGradient id="goldRing2" x1="0" y1="0" x2="1" y2="1">
        <stop offset="0" stop-color="#8a6a35"/>
        <stop offset=".5" stop-color="#e6c98a"/>
        <stop offset="1" stop-color="#b48a45"/>
      </linearGradient>
    </defs>
    <circle cx="99" cy="22" r="166" fill="url(#goldRing2)"/>
    <circle cx="96" cy="19" r="163" fill="var(--ink)"/>
    <path d="M243 529 V214 Q243 196 261 196 H431 Q449 196 449 214 V529 Z" fill="var(--ink)" stroke="url(#goldRing2)" stroke-width="1.5"/>
    <circle cx="346" cy="197" r="63" fill="var(--ink)" stroke="url(#goldRing2)" stroke-width="2"/>
    <path d="M466 -2 V147 Q466 163 482 163 H652 Q668 163 668 147 V-2 Z" fill="var(--ink)" stroke="url(#goldRing2)" stroke-width="1.5"/>
  </svg>

  <p class="brand-name brand-name--panel">Fernhill Wounds</p>
  <div class="pill" style="left:55px;top:200px;width:125px">Mobile Wound Care</div>
  <p class="abs mobile-body">With a focus on convenience, expertise, and<br>compassion, we bring the highest standard<br>of wound care directly to the patient's home.<br>Working side-by-side with the patient’s<br>physician, our team of experienced<br>specialists utilize cutting-edge technology<br>and personalized treatment plans to ensure<br>optimal healing and comfort. From thorough<br>wound assessments to advanced therapies<br>and ongoing support, we prioritize the<br>well-being of our patients every step of the<br>way. Whether it's managing chronic wounds,<br>post-surgery recovery, we go above and<br>beyond to provide comprehensive and<br>compassionate care. With our concierge<br>approach, we aim to make the healing<br>journey as seamless and comfortable as<br>possible, empowering our patients to live<br>their best lives.</p>
  <p class="brand-name brand-name--small" style="left:6px;width:224px;top:467px">Fernhill Wounds</p>

  <p class="abs leaders-title">Leaders in Mobile</p>
  <div class="pill" style="left:275px;top:28px;width:142px;font-size:12px">Advanced Wound Care.</div>
  <p class="abs services-intro">We provide a complete wound<br>management program for our patients that<br>includes the use of advanced treatments, the<br>creation of care plans, and coordination of<br>care with other clinicians. Our comprehensive<br>in-home wound care services include:<br>Advanced Wound Assessment</p>
  <div class="treatment-photo" role="img" aria-label="Photo of a clinician wrapping a bandage around a patient's wrist"></div>
  <ul class="service-list">
    <li>Thorough evaluation of wound<br>type, size, and stage to develop a<br>tailored treatment plan.</li>
    <li>Cutting-Edge Treatments</li>
    <li>Utilization of the latest technologies<br>and techniques in wound care, including:</li>
    <li>Compression</li>
    <li>Biologic Skin Substitutes</li>
    <li>Negative Pressure Wound Therapy</li>
    <li>Collagen and Advanced Dressings</li>
    <li>Surgical/ Trauma Wounds</li>
    <li>Venous/ Arterial Wounds</li>
    <li>Debridements</li>
  </ul>

  <div class="pill pill--outline" style="left:495px;top:19px;width:143px">Personalized Care Plans</div>
  <p class="abs plan-text" style="top:44px">Customized care plans designed to meet<br>the specific needs of each patient,<br>ensuring optimal healing. Coordination<br>and direction of care for other caregivers<br>and clinicians, including home health.</p>
  <p class="abs plan-text" style="top:106px">Patient and Caregiver Education<br>Providing education and support to<br>patients and their caregivers to enhance<br>understanding and promote self-care.</p>

  <div class="pill" style="left:477px;top:177px;width:186px;font-size:11.5px">Partner with Fernhill Wounds:</div>

  <svg class="benefit-icon" style="top:212px" viewBox="0 0 20 20" fill="none" stroke="var(--gold)" stroke-width="1.2" aria-hidden="true"><rect x="3" y="2.5" width="11" height="15" rx="1"/><path d="M6 7 H11 M6 10 H11"/><circle cx="15" cy="15" r="3.5"/><path d="M13.4 15 L14.6 16.2 L16.6 14"/></svg>
  <p class="benefit-title" style="top:216px">Enhanced Patient Outcomes</p>
  <p class="benefit-body" style="top:237px">Our specialized expertise in advanced<br>wound care leads to faster healing times<br>and improved patient satisfaction.</p>
  <div class="benefit-rule" style="top:279px"></div>

  <svg class="benefit-icon" style="top:289px" viewBox="0 0 20 20" fill="none" stroke="var(--gold)" stroke-width="1.2" aria-hidden="true"><circle cx="10" cy="10" r="2.5"/><circle cx="3.5" cy="3.5" r="2"/><circle cx="16.5" cy="3.5" r="2"/><circle cx="3.5" cy="16.5" r="2"/><circle cx="16.5" cy="16.5" r="2"/><path d="M5 5 L8.2 8.2 M15 5 L11.8 8.2 M5 15 L8.2 11.8 M15 15 L11.8 11.8"/></svg>
  <p class="benefit-title" style="top:293px">Extended Reach</p>
  <p class="benefit-body" style="top:314px">Our in-home services allow your patients to<br>receive high-quality care without the need for<br>frequent visits, reducing the burden on<br>your resources.</p>
  <div class="benefit-rule" style="top:364px"></div>

  <svg class="benefit-icon" style="top:376px" viewBox="0 0 20 20" fill="none" stroke="var(--gold)" stroke-width="1.2" aria-hidden="true"><circle cx="10" cy="8" r="6.5"/><path d="M10 4.5 L11 6.8 L13.4 7 L11.6 8.6 L12.1 11 L10 9.8 L7.9 11 L8.4 8.6 L6.6 7 L9 6.8 Z"/><path d="M7 14 L6 19 L10 17 L14 19 L13 14"/></svg>
  <p class="benefit-title" style="top:380px">Professional Integrity</p>
  <p class="benefit-body" style="top:400px">As a trusted partner, we uphold the highest<br>standards of care and professionalism,<br>reflecting positively on your clinic's reputation.</p>
  <div class="benefit-rule" style="top:445px"></div>

  <svg class="benefit-icon" style="top:457px" viewBox="0 0 20 20" fill="none" stroke="var(--gold)" stroke-width="1.2" aria-hidden="true"><rect x="6" y="2" width="10" height="12" rx="1"/><path d="M9 6 H13 M9 9 H13"/><rect x="2" y="10" width="9" height="7" rx="1"/></svg>
  <p class="benefit-title" style="top:461px">Seamless Collaboration</p>
  <p class="benefit-body" style="top:481px">We maintain open communication with referring<br>clinics, ensuring a coordinated approach to<br>patient care.</p>

  <div class="fold fold--left"></div>
  <div class="fold fold--mid"></div>
</section>

</body>
</html>
```